BRIMCOVE is a New Zealand based aerial imaging company performing mapping, surveying and videography

I would like a business card that is contemporary and clean. The font for the business name is called Gtec Technology and I would like to have the text "AERIAL IMAGING" under the "BRIMCOVE" name in a font similar to URW Gothic or another light modern font. Brimcove performs aerial imaging projects using a hexacopter UAV. Surveying and mapping with 3D Digital Elevation Models are a focus, I also produce aerial photographs and video's including post editing.

Target Market(s)

Industrial plant managers, Property owners, Event organisers.

Industry/Entity Type

Videography

Contact Information for Business Card

BRIMCOVE AERIAL IMAGING. Owner Reid Malloway. Cell: 021 7304169. P.O. Box 8316 Dunedin, New Zealand.

Font styles to use
Other font styles liked:
• Gtec Technology

Colors
9bcb3b
33a6d7
ec1f27

Requirements
Must have
• Modern professional look.
Nice to have
• Perhaps an aerial image of a landscape who's location is not identifiable. Maybe use included image of my hexacopter on the back of the card? Not compulsory though.
Should not have
• Clip Art style images.

```html
<!DOCTYPE html>
<html lang="en">
<head>
<meta charset="utf-8">
<title>Brimcove Aerial Imaging – Business Card</title>
<link rel="stylesheet" href="https://fonts.googleapis.com/css2?family=Questrial&family=Montserrat:wght@600&display=swap">
<style>
  :root {
    --page: #ffffff;
    --ink: #111111;
    --brand-green: #8dc63f;
    --brand-gray: #5b5b5d;
    --card-dark: #3b3b3d;
    --frame-dark: #454547;
    --tag-blue: #5ccbed;
    --tag-red: #ec2a2a;
    --tag-green: #9bcb3b;
    --white: #ffffff;
  }
  html, body {
    margin: 0;
    padding: 0;
    overflow: hidden;
    background: var(--page);
  }
  .canvas {
    position: relative;
    width: 1200px;
    height: 454px;
    overflow: hidden;
    background: var(--page);
    font-family: "Questrial", "Helvetica Neue", Arial, sans-serif;
  }

  /* ---------- Front card ---------- */
  .card-front {
    position: absolute;
    left: 38px;
    top: 35px;
    width: 545px;
    height: 339px;
    border: 1px solid var(--ink);
    background: var(--white);
    overflow: hidden;
  }
  .brand {
    position: absolute;
    left: 0;
    right: 0;
    top: 44px;
    text-align: center;
  }
  .brand-name {
    display: block;
    font-size: 46px;
    line-height: 48px;
    letter-spacing: 3px;
    color: var(--brand-green);
  }
  .brand-tagline {
    display: block;
    margin-top: 2px;
    font-size: 22px;
    letter-spacing: 5px;
    color: var(--brand-gray);
  }
  .accent-band {
    position: absolute;
    left: 0;
    right: 0;
    top: 128px;
    height: 10px;
    background: linear-gradient(90deg, #7a7a7a 0%, #a6bf7c 40%, var(--brand-green) 100%);
  }
  .contact-panel {
    position: absolute;
    left: 0;
    right: 0;
    top: 138px;
    bottom: 0;
    background: var(--card-dark);
    text-align: center;
  }
  .person-name {
    margin: 34px 0 0;
    font-size: 21px;
    font-weight: 700;
    letter-spacing: 0.5px;
    color: var(--brand-green);
  }
  .person-role {
    margin: 3px 0 0;
    font-size: 13px;
    color: var(--white);
  }
  .person-phone {
    margin: 6px 0 0;
    font-size: 18px;
    letter-spacing: 0.5px;
    color: var(--brand-green);
  }
  .address-line {
    position: absolute;
    left: 0;
    right: 0;
    bottom: 10px;
    margin: 0;
    font-size: 15px;
    letter-spacing: 0.3px;
    color: var(--white);
  }
  .address-line .divider {
    color: var(--brand-green);
    margin: 0 6px;
  }

  /* ---------- Back card ---------- */
  .card-back {
    position: absolute;
    left: 618px;
    top: 35px;
    width: 547px;
    height: 341px;
    background: var(--frame-dark);
    border: 1px solid var(--ink);
    box-sizing: border-box;
    overflow: hidden;
  }
  .aerial-photo {
    position: absolute;
    left: 2px;
    right: 2px;
    top: 19px;
    height: 270px;
    background: linear-gradient(180deg,
      #aebfd6 0%, #c3cfe0 30%, #8f98a8 48%, #5f6f73 58%,
      #7f9aa8 66%, #4e6b3a 78%, #3f5a2a 100%);
  }
  .service-tags {
    position: absolute;
    left: 2px;
    right: 2px;
    top: 221px;
    display: flex;
    flex-direction: column;
    gap: 1px;
    padding: 0 6px;
    line-height: 22px;
    white-space: nowrap;
  }
  .tag-row {
    display: flex;
    justify-content: space-between;
    align-items: baseline;
  }
  .tag-blue { color: var(--tag-blue); }
  .tag-red { color: var(--tag-red); }
  .tag-green { color: var(--tag-green); }
  .tag-lg { font-size: 22px; }
  .tag-md { font-size: 19px; }
  .tag-sm { font-size: 16px; }
  .back-band {
    position: absolute;
    left: 2px;
    right: 2px;
    top: 289px;
    height: 6px;
    background: linear-gradient(90deg, #6f8f40 0%, var(--brand-green) 100%);
  }

  /* ---------- Labels ---------- */
  .view-label {
    position: absolute;
    top: 402px;
    margin: 0;
    font-family: "Montserrat", Arial, sans-serif;
    font-weight: 600;
    font-size: 19px;
    letter-spacing: 2px;
    color: var(--ink);
  }
  .label-front { left: 56px; }
  .label-back { left: 655px; }
</style>
</head>
<body>
<main class="canvas">

  <section class="card-front">
    <div class="brand">
      <span class="brand-name">BRIMCOVE</span>
      <span class="brand-tagline">Aerial Imaging</span>
    </div>
    <div class="accent-band"></div>
    <div class="contact-panel">
      <p class="person-name">Reid Malloway</p>
      <p class="person-role">Owner</p>
      <p class="person-phone">Cell: 021 7304169</p>
      <p class="address-line">BRIMCOVE AERIAL IMAGING<span class="divider">|</span>P.O. Box 8316 Dunedin, New Zealand</p>
    </div>
  </section>

  <section class="card-back">
    <div class="aerial-photo" role="img" aria-label="Photograph of a hexacopter drone hovering over a green hill with a lake and misty mountains behind"></div>
    <div class="service-tags">
      <div class="tag-row">
        <span class="tag-blue tag-md">Brimcove</span>
        <span class="tag-green tag-lg">hexacopter flights</span>
        <span class="tag-red tag-sm">post editing</span>
        <span class="tag-blue tag-md">site surveys</span>
      </div>
      <div class="tag-row">
        <span class="tag-red tag-sm">mapping</span>
        <span class="tag-blue tag-lg">3D elevation models</span>
        <span class="tag-green tag-md">event video</span>
      </div>
      <div class="tag-row">
        <span class="tag-green tag-sm">property</span>
        <span class="tag-blue tag-md">industrial plant</span>
        <span class="tag-red tag-md">aerial stills</span>
        <span class="tag-green tag-lg">UAV</span>
      </div>
    </div>
    <div class="back-band"></div>
  </section>

  <h2 class="view-label label-front">FRONT CARD DESIGN</h2>
  <h2 class="view-label label-back">BACK CARD DESIGN</h2>

</main>
</body>
</html>
```